Business Cards and stationary for personal wealth management company
Quillmere Capital
Creative Brief
Simple
Martin J Hollis, CRPC®
President | Wealth Management
4471 SW Alder Ave Ste 115 Bellevue, WA 98007
martin.hollis@qvm-example.com
www.stoneharborcapital-example.com
>> I need a 2 sided business card and supporting stationary. disclosure: I am thinking of using the disclosure language noted below - at the bottom of the backside of the business card. Securities offered through QVM Securities, member NASTRO/CIRF Also - On the back of the business card - I would like to consider a watermarked image on a darker background with the text in a lighter font. Also - I want to consider a tagline on the front: not sure I will use a tagline though. Tagline idea: Putting Your Wealth to Work for You! (or) Our Independence - Your Advantage!
Our Mission Our purpose is to deliver exceptional financial guidance and personalized service to help you build and preserve your wealth, create a strategy for passing on a lasting heritage to loved ones or meaningful charities, and empower you to pursue your life’s aspirations. Our Independence - Your Advantage! Quillmere is uniquely positioned to cater to your distinct financial needs. As your trusted financial advocate, we provide unbiased investment guidance and financial planning to help you manage your wealth over your lifetime and beyond. We have no proprietary investment products to sell and no investment banking relationships to promote. Putting Your Wealth to Work for You! We start by gaining a deep understanding of your values, goals and unique perspectives. Once we have insight into your distinct financial situation, we begin to design a highly customized, integrated wealth management solution.

```html
<!DOCTYPE html>
<html lang="en">
<head>
<meta charset="utf-8">
<title>Quillmere Capital – Business Card</title>
<link href="https://fonts.googleapis.com/css2?family=Cinzel:wght@600&family=Montserrat:wght@400;600&display=swap" rel="stylesheet">
<style>
  :root {
    --backdrop: #d6d7da;
    --card: #ffffff;
    --navy: #2c3a68;
    --panel: #3e5185;
    --panel-line: rgba(255,255,255,0.35);
    --ink-light: #ffffff;
    --ink-muted: #5a6280;
  }
  * { box-sizing: border-box; margin: 0; padding: 0; }
  html, body { width: 1200px; height: 895px; overflow: hidden; }
  body {
    background: var(--backdrop);
    font-family: "Montserrat", Arial, sans-serif;
    position: relative;
  }
  .card {
    position: absolute;
    top: 292px;
    width: 540px;
    height: 310px;
    background: var(--card);
    box-shadow: 0 6px 18px rgba(0,0,0,0.15);
    overflow: hidden;
  }
  .card--front { left: 40px; }
  .card--back { left: 620px; }

  .brand {
    position: absolute;
    display: flex;
    align-items: center;
    gap: 10px;
    color: var(--navy);
    font-family: "Cinzel", Georgia, serif;
    font-weight: 600;
  }
  .brand__mark { width: 14px; height: 14px; background: var(--navy); flex: none; }
  .brand__name { display: flex; flex-direction: column; line-height: 1; }
  .brand__main { font-size: 30px; letter-spacing: 1px; }
  .brand__sub { font-size: 12px; letter-spacing: 10px; margin-top: 4px; padding-left: 40px; }
  .card--front .brand { left: 28px; top: 30px; }
  .card--back .brand { left: 110px; top: 118px; }
  .card--back .brand__main { font-size: 36px; }
  .card--back .brand__sub { font-size: 14px; letter-spacing: 12px; padding-left: 52px; }

  .accent-tab { position: absolute; right: 0; width: 150px; height: 20px; }
  .card--front .accent-tab { top: 98px; }
  .card--back .accent-tab { top: 34px; width: 170px; }

  .holder {
    position: absolute;
    right: 26px;
    top: 128px;
    text-align: right;
    color: var(--navy);
  }
  .holder__name { font-size: 14px; font-weight: 600; letter-spacing: 1.5px; text-transform: uppercase; }
  .holder__title { font-size: 9px; letter-spacing: 1px; margin-top: 3px; color: var(--ink-muted); text-transform: uppercase; }

  .contact-panel {
    position: absolute;
    left: 18px;
    right: 18px;
    top: 172px;
    bottom: 18px;
    background: var(--panel);
    border-radius: 10px;
    display: grid;
    grid-template-columns: 140px 1fr 150px;
    color: var(--ink-light);
  }
  .contact-item {
    display: flex;
    flex-direction: column;
    align-items: center;
    justify-content: center;
    gap: 10px;
    padding: 0 8px;
    text-align: center;
    font-size: 9.5px;
    line-height: 1.6;
    white-space: nowrap;
  }
  .contact-item + .contact-item { border-left: 1px solid var(--panel-line); }
  .contact-item svg { width: 24px; height: 24px; }
</style>
</head>
<body>
  <section class="card card--front" aria-label="Business card front">
    <div class="brand">
      <span class="brand__mark"></span>
      <span class="brand__name">
        <span class="brand__main">QUILLMERE</span>
        <span class="brand__sub">CAPITAL</span>
      </span>
    </div>
    <svg class="accent-tab" viewBox="0 0 150 20" preserveAspectRatio="none" aria-hidden="true">
      <polygon points="14,0 150,0 150,20 0,20" fill="var(--panel)"/>
    </svg>
    <div class="holder">
      <p class="holder__name">Odell Tamsworth</p>
      <p class="holder__title">President | Wealth Management</p>
    </div>
    <div class="contact-panel">
      <div class="contact-item contact-item--phone">
        <svg viewBox="0 0 24 24" aria-hidden="true"><path fill="#fff" d="M6.6 10.8a15.1 15.1 0 0 0 6.6 6.6l2.2-2.2c.3-.3.7-.4 1-.2 1.1.4 2.3.6 3.6.6.6 0 1 .4 1 1V20c0 .6-.4 1-1 1A17 17 0 0 1 3 4c0-.6.4-1 1-1h3.5c.6 0 1 .4 1 1 0 1.3.2 2.5.6 3.6.1.3 0 .7-.2 1z"/></svg>
        <p>012 555 0148<br>012 555 0149</p>
      </div>
      <div class="contact-item contact-item--web">
        <svg viewBox="0 0 24 24" aria-hidden="true" fill="none" stroke="#fff" stroke-width="1.6"><circle cx="12" cy="12" r="9"/><ellipse cx="12" cy="12" rx="4" ry="9"/><line x1="3" y1="12" x2="21" y2="12"/><path d="M5 7.5h14M5 16.5h14"/></svg>
        <p>o.tamsworth@quillmere-example.com<br>www.quillmere-example.com</p>
      </div>
      <div class="contact-item contact-item--address">
        <svg viewBox="0 0 24 24" aria-hidden="true"><path fill="#fff" d="M12 2a7 7 0 0 0-7 7c0 5.2 7 13 7 13s7-7.8 7-13a7 7 0 0 0-7-7zm0 9.5A2.5 2.5 0 1 1 12 6.5a2.5 2.5 0 0 1 0 5z"/></svg>
        <p>4471 Fenwick Row Ste 115<br>Larkvale, ZN 00417</p>
      </div>
    </div>
  </section>

  <section class="card card--back" aria-label="Business card back">
    <svg class="accent-tab" viewBox="0 0 170 20" preserveAspectRatio="none" aria-hidden="true">
      <polygon points="14,0 170,0 170,20 0,20" fill="var(--panel)"/>
    </svg>
    <div class="brand">
      <span class="brand__mark"></span>
      <span class="brand__name">
        <span class="brand__main">QUILLMERE</span>
        <span class="brand__sub">CAPITAL</span>
      </span>
    </div>
  </section>
</body>
</html>
```